Business Cards for Retail/Sourcing Business.

We need a business cards for our company where it looks like:
TK
LM

VERTICAL, where the TK is over the LM. Then Under the TKLM would be name, address and website address. We want the P to be in the style of our original logo, which I uploaded.

Also, can we get a couple of designs with fun colors - especially for the letter head.

Target Market(s)

Old clients. Many of our clients or people we do business with are 40-50 plus. We are not an industry with many young people.

Industry/Entity Type

Business

Contact Information for Business Card

Front side is just says TKLM with name, title, address, and website below.

Font styles to use
Serif
Sans Serif
Decorative
Script

Requirements
Must have
• THE TKLM design with the P in the design of the logo
Nice to have
• Fun colors, new takes on the TKLM and any other additions that would be cool and make it pop

```html
<!DOCTYPE html>
<html lang="en">
<head>
<meta charset="utf-8">
<title>TKLM Business Cards</title>
<link href="https://fonts.googleapis.com/css2?family=PT+Serif:wght@400;700&display=swap" rel="stylesheet">
<style>
  :root {
    --stage: #e9e6e1;
    --card-light: #fbfbfb;
    --card-mid: #e4e4e4;
    --band: rgba(0, 0, 0, 0.045);
    --ink: #141414;
    --text: #3a3a3a;
    --shadow: rgba(0, 0, 0, 0.28);
  }
  html, body {
    margin: 0;
    padding: 0;
    width: 1200px;
    height: 885px;
    overflow: hidden;
    background: var(--stage);
  }
  .stage {
    position: relative;
    width: 1200px;
    height: 885px;
  }
  .card {
    position: absolute;
    width: 540px;
    height: 310px;
    border-radius: 16px;
    overflow: hidden;
    background: linear-gradient(135deg, var(--card-light) 0%, #f1f1f1 45%, var(--card-mid) 100%);
    box-shadow: 0 3px 0 #d6d6d6, 0 6px 0 #cfcfcf, 0 9px 0 #c8c8c8, 0 22px 38px var(--shadow);
  }
  .card-front { left: 70px; top: 110px; }
  .card-back { left: 590px; top: 455px; }
  .band {
    position: absolute;
    top: 0;
    bottom: 0;
    background: var(--band);
  }
  .card-front .band-one { left: 60px; width: 34px; }
  .card-front .band-two { left: 250px; width: 22px; }
  .card-back .band-one { left: 110px; width: 40px; }
  .card-back .band-two { left: 390px; width: 26px; }
  .wordmark {
    position: absolute;
    font-family: "PT Serif", serif;
    font-weight: 700;
    color: var(--ink);
    line-height: 0.86;
    margin: 0;
  }
  .card-front .wordmark {
    left: 40px;
    bottom: 36px;
    font-size: 118px;
  }
  .card-back .wordmark {
    left: 0;
    right: 0;
    top: 42px;
    text-align: center;
    font-size: 128px;
  }
  .wordmark span { display: block; }
  .contact {
    position: absolute;
    left: 300px;
    top: 40px;
    right: 24px;
    font-family: "PT Serif", serif;
    color: var(--text);
    font-size: 13px;
    line-height: 1.4;
  }
  .contact-name {
    font-size: 24px;
    color: var(--text);
    margin: 0;
    font-weight: 400;
    line-height: 1.1;
  }
  .contact-title { margin: 2px 0 18px; }
  .contact-address { margin: 0 0 18px; }
  .contact-lines { margin: 0; }
</style>
</head>
<body>
<main class="stage">
  <section class="card card-front" aria-label="Business card front">
    <div class="band band-one"></div>
    <div class="band band-two"></div>
    <h1 class="wordmark"><span>TK</span><span>LM</span></h1>
    <div class="contact">
      <p class="contact-name">Marlo Fenwick</p>
      <p class="contact-title">Home, Sourcing</p>
      <p class="contact-address">482 Larkspur Avenue,<br>Fairhaven 20417 United States</p>
      <p class="contact-lines">+15550142790<br>hello@tklmtrading.com<br>tklmtrading.example.com</p>
    </div>
  </section>

  <section class="card card-back" aria-label="Business card back">
    <div class="band band-one"></div>
    <div class="band band-two"></div>
    <p class="wordmark"><span>TK</span><span>LM</span></p>
  </section>
</main>
</body>
</html>
```